International IT Business Needs a Proffesional and Innovative Business Card

We need a proffesional and innovative business card for a new company based in Venezuela called 'QuillonMark'. We are RVK Business Partner, RVK is a key manufacture for us, one of the most influential players in technology, and the leader in cloud computing, virtualization, Big Data storage and analytics, and IT security and protection.

RVK has developed a global network of business partners to bring customers the full complement of skills and expertise required to build their information infrastructures. This partner ecosystem helps customers maximize the value of their information at the lowest total cost.

We would like to see designs that use the RVK Business Partnet logo & QuillonMark logo.

http://brand.rvk-example.com/BrandGuide/partners/rvk-business-partner-logo/

Thank you in advance for your interest.

Happy Day!!!! I look forward to your creative design!!!

Thank you in advance.

Marisol Quevedo

Target Market(s)

QuillonMark's target markets include large companies and small- and medium-sized businesses across various vertical markets.

Industry/Entity Type

Security

Font styles to use
Other font styles liked:
• We use Meta as the RVK® corporate font.

Colors

Designer to choose colors to be used in the design.

Requirements
Must have
• Name
Title
Address
web page (www.quillon-example.la)

Nice to have
• Add a QR code on the reverse of the card.

```html
<!DOCTYPE html>
<html lang="en">
<head>
<meta charset="utf-8">
<title>QuillonMark Business Card</title>
<link rel="stylesheet" href="https://fonts.googleapis.com/css2?family=Open+Sans:wght@400;600;700&family=Libre+Baskerville:wght@400;700&display=swap">
<style>
  :root {
    --bg: #ecebe8;
    --paper: #ffffff;
    --paper-back: #f1f1f1;
    --navy: #2d2360;
    --lavender: #8f8bb0;
    --green: #3fb23a;
    --green-light: #a9dd8a;
    --green-mint: #86d69a;
    --silver: #c9c9c9;
    --ink-light: #f2f2f7;
    --icon: #b6e06a;
    --name-blue: #3e4f96;
    --title-green: #8bbf3f;
  }
  * { box-sizing: border-box; margin: 0; padding: 0; }
  html, body { width: 1200px; height: 900px; overflow: hidden; }
  body { background: var(--bg); font-family: "Open Sans", sans-serif; position: relative; }

  .card {
    position: absolute; left: 240px; width: 720px; height: 400px;
    background: var(--paper); overflow: hidden;
    box-shadow: 0 6px 18px rgba(0,0,0,.15);
  }
  .card--front { top: 30px; }
  .card--back { top: 470px; background: linear-gradient(160deg, #fafafa, var(--paper-back)); }

  .wordmark { display: flex; align-items: center; gap: 10px; }
  .wordmark__dot { width: 18px; height: 18px; border-radius: 50%; background: var(--green); flex: none; }
  .wordmark__name { font-family: "Open Sans", sans-serif; font-weight: 700; color: var(--navy); letter-spacing: -.5px; white-space: nowrap; }

  .card--front .wordmark { position: absolute; left: 50px; top: 58px; }
  .card--front .wordmark__name { font-size: 36px; }

  .person { position: absolute; right: 56px; top: 96px; text-align: right; font-family: "Libre Baskerville", serif; }
  .person__name { font-size: 24px; font-weight: 700; color: var(--name-blue); letter-spacing: .5px; }
  .person__title { font-size: 13px; color: var(--title-green); margin-top: 2px; }

  .contact-band {
    position: absolute; left: 0; top: 170px; width: 100%; height: 150px;
    background: linear-gradient(90deg, var(--lavender) 0 30%, var(--navy) 30% 76%, var(--lavender) 76% 100%);
    color: var(--ink-light); font-size: 13px; line-height: 1.7;
  }
  .contact { position: absolute; display: grid; grid-template-columns: 16px auto; column-gap: 8px; align-items: center; white-space: nowrap; }
  .contact svg { width: 13px; height: 13px; }
  .contact--address { left: 36px; top: 22px; }
  .contact--phones { left: 270px; top: 62px; }
  .contact--online { left: 490px; top: 92px; }

  .stripe { position: absolute; left: 0; width: 100%; height: 12px;
    background: repeating-linear-gradient(180deg, var(--silver) 0 2px, #f4f4f4 2px 4px); }
  .green-band { position: absolute; left: 0; width: 100%;
    background: linear-gradient(90deg, var(--green-mint) 0%, var(--green) 35%, #6cc63d 70%, var(--green-light) 100%); }
  .card--front .stripe { top: 320px; }
  .card--front .green-band { top: 332px; height: 68px; }

  .card--back .wordmark { position: absolute; left: 50%; top: 110px; transform: translateX(-50%); }
  .card--back .wordmark__dot { width: 26px; height: 26px; }
  .card--back .wordmark__name { font-size: 52px; }
  .card--back .stripe { top: 288px; }
  .card--back .green-band { top: 300px; height: 100px; }
</style>
</head>
<body>

<section class="card card--front" aria-label="Business card front">
  <div class="wordmark">
    <span class="wordmark__dot"></span>
    <span class="wordmark__name">QuillonMark</span>
  </div>

  <div class="person">
    <p class="person__name">JOHN DOE</p>
    <p class="person__title">Graphic Designer</p>
  </div>

  <div class="contact-band">
    <div class="contact contact--address">
      <svg viewBox="0 0 12 12"><path d="M6 0.5a4 4 0 0 0-4 4c0 3 4 7 4 7s4-4 4-7a4 4 0 0 0-4-4z" fill="var(--icon)"/><circle cx="6" cy="4.5" r="1.5" fill="var(--lavender)"/></svg>
      <span>48 Maplerow Ave.</span>
      <span></span><span>Westbrook NY 10987</span>
    </div>
    <div class="contact contact--phones">
      <svg viewBox="0 0 12 12"><path d="M3 1l2 2-1 1.5c.6 1.4 1.6 2.4 3 3L8.5 6.5l2 2L9 10.5C5 10 2 7 1.5 3z" fill="var(--icon)"/></svg>
      <span>+(000) 555 0142</span>
      <svg viewBox="0 0 12 12"><rect x="2" y="1" width="6" height="4" fill="var(--icon)"/><rect x="1" y="5" width="10" height="6" fill="var(--icon)"/><rect x="3" y="7" width="6" height="1" fill="var(--navy)"/></svg>
      <span>+(000) 555 0143</span>
    </div>
    <div class="contact contact--online">
      <svg viewBox="0 0 12 12"><circle cx="6" cy="6" r="5" fill="none" stroke="var(--icon)" stroke-width="1.3"/><path d="M1 6h10M6 1c-2.5 3-2.5 7 0 10M6 1c2.5 3 2.5 7 0 10" fill="none" stroke="var(--icon)" stroke-width="1"/></svg>
      <span>www.quillon-example.la</span>
      <svg viewBox="0 0 12 12"><rect x="1" y="2.5" width="10" height="7" fill="none" stroke="var(--icon)" stroke-width="1.2"/><path d="M1 2.5l5 4 5-4" fill="none" stroke="var(--icon)" stroke-width="1.2"/></svg>
      <span>john.doe@mail-example.com</span>
    </div>
  </div>

  <div class="stripe"></div>
  <div class="green-band"></div>
</section>

<section class="card card--back" aria-label="Business card back">
  <div class="wordmark">
    <span class="wordmark__dot"></span>
    <span class="wordmark__name">QuillonMark</span>
  </div>
  <div class="stripe"></div>
  <div class="green-band"></div>
</section>

</body>
</html>
```